Lanterne architecture business cards

We are a new company based in New Zealand. We Specialize in High end Luxury Residential Architecture.

Every home is bespoke and is designed to each clients individual requirements and needs.

I like to design buildings that inspire people through light and form while offering a high level of comfort and usability.

Lines of sight, proportion and balance are fundamental to the spaces I create.
Updates

August 5th is current deadline - Today's date is the 13th of August.

Target Market(s)

New Zealanders who want a custom individual home design, typically 30-65 year old males and females

Industry/Entity Type

Architecture

Contact Information for Business Card

Director - Derek Tolson
Contact Number - 0279164073
Email - info@lanternearchitecture-example.co.nz
Webstie - www.lanternearchitecture-example.co.nz
Social Media - @lanternearchitecture

Font styles to use
Sans Serif

Requirements
Must have
• Logo (Both Sides)
Website
Email
Contact Number
Social Media

Nice to have
• Texture
Should not have
• More than 3 colours - typically I would've thought 2 would be good to match the logo.

```html
<!DOCTYPE html>
<html lang="en">
<head>
<meta charset="utf-8">
<title>Lanterne architecture business cards</title>
<link rel="stylesheet" href="https://fonts.googleapis.com/css2?family=Montserrat:wght@300;400;500&display=swap">
<style>
  :root {
    --page: #3a3a3a;
    --card-light: #ffffff;
    --card-shade: #e4e4e4;
    --plate: #ececec;
    --ink: #1e1e1e;
    --ink-soft: #4a4a4a;
    --ink-muted: #6a6a6a;
  }
  * { box-sizing: border-box; margin: 0; padding: 0; }
  html, body {
    width: 1200px; height: 997px; overflow: hidden;
    background: var(--page);
    font-family: "Montserrat", Arial, sans-serif;
  }
  .sheet {
    width: 1200px; height: 997px;
    display: flex; flex-direction: column;
    align-items: center; justify-content: center; gap: 56px;
  }
  .card {
    position: relative;
    width: 720px; height: 411px;
    background: linear-gradient(135deg, var(--card-light) 0%, #f4f4f4 55%, var(--card-shade) 100%);
    box-shadow: 0 12px 30px rgba(0,0,0,.45);
    overflow: hidden;
  }
  .plate {
    position: absolute; border-radius: 50%;
    background: radial-gradient(circle at 45% 40%, #f7f7f7, var(--plate));
  }
  .brand {
    position: absolute; display: flex; align-items: center; gap: 12px;
    color: var(--ink); font-weight: 400; font-size: 20px;
    letter-spacing: .18em; text-transform: uppercase; white-space: nowrap;
  }
  .brand-dot {
    width: 14px; height: 14px; border-radius: 50%; background: var(--ink);
  }
  /* back */
  .card--back .plate { width: 300px; height: 300px; left: 210px; top: 55px; }
  .card--back .brand { left: 0; right: 0; top: 168px; justify-content: center; }
  .handle {
    position: absolute; left: 0; right: 0; top: 232px; text-align: center;
    font-size: 15px; font-weight: 400; color: var(--ink-soft); letter-spacing: .02em;
  }
  /* front */
  .card--front .plate { width: 290px; height: 290px; left: 380px; top: 30px; }
  .card--front .brand { left: 380px; width: 290px; top: 162px; justify-content: center; font-size: 18px; }
  .person { position: absolute; left: 48px; top: 200px; }
  .person-name {
    font-size: 22px; font-weight: 500; color: var(--ink); text-transform: uppercase; letter-spacing: .01em;
  }
  .person-role {
    font-size: 14px; font-weight: 400; color: var(--ink-muted); text-transform: uppercase; letter-spacing: .04em;
  }
  .contacts { position: absolute; left: 48px; top: 298px; list-style: none; }
  .contacts li {
    display: flex; align-items: center; gap: 14px; height: 26px;
    font-size: 15px; font-weight: 300; color: var(--ink-soft);
  }
  .contacts svg { width: 16px; height: 16px; flex: none; }
</style>
</head>
<body>
<main class="sheet">
  <section class="card card--back" aria-label="Card back">
    <div class="plate"></div>
    <div class="brand"><span class="brand-dot"></span>Lanterne architecture</div>
    <p class="handle">@lanternearchitecture</p>
  </section>

  <section class="card card--front" aria-label="Card front">
    <div class="plate"></div>
    <div class="brand"><span class="brand-dot"></span>Lanterne architecture</div>
    <div class="person">
      <p class="person-name">Derek Tolson</p>
      <p class="person-role">Director</p>
    </div>
    <ul class="contacts">
      <li>
        <svg viewBox="0 0 16 16" aria-hidden="true"><path d="M2 6c0-2 3-3 6-3s6 1 6 3v1h-3V5.5H5V7H2z M3.5 8h9l1 5h-11z" fill="#2a2a2a"/></svg>
        0279164073
      </li>
      <li>
        <svg viewBox="0 0 16 16" aria-hidden="true"><rect x="1" y="3.5" width="14" height="9" fill="#2a2a2a"/><path d="M1.5 4l6.5 5 6.5-5" fill="none" stroke="#fff" stroke-width="1"/></svg>
        info@lanternearchitecture-example.co.nz
      </li>
      <li>
        <svg viewBox="0 0 16 16" aria-hidden="true"><circle cx="8" cy="8" r="6.5" fill="#2a2a2a"/><path d="M1.5 8h13M8 1.5c-3 3.5-3 9.5 0 13M8 1.5c3 3.5 3 9.5 0 13" fill="none" stroke="#fff" stroke-width=".8"/></svg>
        www.lanternearchitecture-example.co.nz
      </li>
    </ul>
  </section>
</main>
</body>
</html>
```